Tidewell Crest Housekeeping Ovu

I am looking for a car wrap design. I do not want to wrap the whole car. Id like to wrap the sides, some on the back and the hood. I am uploading a general idea of what im looking for. I’d prefer more white space than less. I’d like it to be fun without being funny or gimmicky. Back window can have some writing on it. In the examples I shared, I like the simplicity of them. It is a 2011 Ovu Palmero.

Target Market(s)

Families. We give back time to enjoy life

Industry/Entity Type

Residential cleaning

Font styles to use
Sans Serif

Colors
0054AA
0677BA
7BADD7
CADEEF
E8F1F8
E54698
E96AAD
F1A4CE
F9D9EA
FCEFF6

Requirements
Must have
• Please ck website www.tidewellcresthousekeeping.com for content and ideas. I’d like whatever is on the good to be backwards.
Should not have
• No charicaturest or cartoony stuff

```html
<!DOCTYPE html>
<html lang="en">
<head>
<meta charset="utf-8">
<title>Tidewell Crest Housekeeping – Side Door Wrap Panels</title>
<link rel="stylesheet" href="https://fonts.googleapis.com/css2?family=Poppins:ital,wght@0,300;0,600;0,700;1,800&display=swap">
<style>
  :root {
    --page: #ffffff;
    --wrap-blue-light: #45b0f0;
    --wrap-blue: #1f8fe0;
    --wrap-blue-deep: #1479c9;
    --name-blue: #1a22b4;
    --pink: #e54698;
    --pink-soft: #e96aad;
    --strip: #f3f4f7;
    --ink-shadow: rgba(0, 40, 90, 0.18);
  }
  * { box-sizing: border-box; margin: 0; padding: 0; }
  html, body {
    width: 1200px;
    height: 1072px;
    overflow: hidden;
    background: var(--page);
    font-family: "Poppins", sans-serif;
  }
  .wrap-sheet {
    position: relative;
    width: 1200px;
    height: 1072px;
  }
  .door-panel {
    position: absolute;
    left: 110px;
    width: 980px;
    height: 440px;
    border-radius: 14px;
    background: linear-gradient(160deg, var(--wrap-blue-light) 0%, var(--wrap-blue) 55%, var(--wrap-blue-deep) 100%);
    box-shadow: 0 6px 18px var(--ink-shadow);
    overflow: hidden;
  }
  .door-panel--driver { top: 62px; }
  .door-panel--passenger { top: 566px; }

  .phone-tag {
    position: absolute;
    top: 30px;
    display: flex;
    align-items: center;
    gap: 10px;
    height: 54px;
    padding: 0 26px 0 18px;
    background: var(--strip);
    border-radius: 6px;
    color: var(--pink);
    font-weight: 800;
    font-style: italic;
    font-size: 34px;
    letter-spacing: 0.5px;
  }
  .door-panel--driver .phone-tag { right: 34px; }
  .door-panel--passenger .phone-tag { left: 34px; }
  .phone-tag svg { width: 30px; height: 30px; flex: none; }

  .brand-block {
    position: absolute;
    left: 92px;
    top: 118px;
    display: flex;
    align-items: center;
    gap: 30px;
  }
  .door-panel--passenger .brand-block { left: 150px; top: 128px; }
  .brand-square {
    width: 150px;
    height: 150px;
    background: var(--pink);
    flex: none;
  }
  .brand-name {
    color: var(--name-blue);
    font-weight: 700;
    font-size: 62px;
    line-height: 1.02;
  }
  .tagline {
    margin-top: 6px;
    color: var(--pink-soft);
    font-weight: 300;
    font-size: 30px;
  }

  .web-strip {
    position: absolute;
    left: 80px;
    bottom: 34px;
    width: 760px;
    height: 50px;
    display: flex;
    align-items: center;
    justify-content: center;
    background: var(--strip);
    border-radius: 4px;
    color: var(--pink);
    font-weight: 800;
    font-style: italic;
    font-size: 28px;
  }
  .door-panel--passenger .web-strip { left: 140px; }
</style>
</head>
<body>
<main class="wrap-sheet">

  <section class="door-panel door-panel--driver" aria-label="Driver side door wrap">
    <div class="phone-tag">
      <svg viewBox="0 0 24 24" aria-hidden="true"><circle cx="12" cy="12" r="12" fill="#e54698"/><path d="M8.2 6.5l1.8-.4 1.2 2.8-1.3 1a7 7 0 003.2 3.2l1-1.3 2.8 1.2-.4 1.8c-.2.7-.8 1.1-1.5 1a9.5 9.5 0 01-7.8-7.8c-.1-.7.3-1.3 1-1.5z" fill="#fff"/></svg>
      610-555-0192
    </div>
    <div class="brand-block">
      <div class="brand-square"></div>
      <div>
        <p class="brand-name">Tidewell Crest<br>Housekeeping</p>
        <p class="tagline">leave the DIRTY work to us!</p>
      </div>
    </div>
    <div class="web-strip">www.TidewellCrestHousekeeping.com</div>
  </section>

  <section class="door-panel door-panel--passenger" aria-label="Passenger side door wrap">
    <div class="phone-tag">
      <svg viewBox="0 0 24 24" aria-hidden="true"><circle cx="12" cy="12" r="12" fill="#e54698"/><path d="M8.2 6.5l1.8-.4 1.2 2.8-1.3 1a7 7 0 003.2 3.2l1-1.3 2.8 1.2-.4 1.8c-.2.7-.8 1.1-1.5 1a9.5 9.5 0 01-7.8-7.8c-.1-.7.3-1.3 1-1.5z" fill="#fff"/></svg>
      610-555-0192
    </div>
    <div class="brand-block">
      <div class="brand-square"></div>
      <div>
        <p class="brand-name">Tidewell Crest<br>Housekeeping</p>
        <p class="tagline">leave the DIRTY work to us!</p>
      </div>
    </div>
    <div class="web-strip">www.TidewellCrestHousekeeping.com</div>
  </section>

</main>
</body>
</html>
```